Header/Logo Redesign

****WE HAVE FOUND THE DESIGNER WHO WILL BE HANDLING THIS PROJECT. PLEASE DONT SUBMIT ANY MORE DESIGNS.****
We have been working with a Web/Logo Designer on a new header and logo for our site. We like some of it, but other things need changing.
Overall Look: We are looking for something that is professional, yet still fresh. Most business two business websites seem old fashinoned. The site we like most is www.tallyhaven.com.
Header Thoughts:
-We like the color at the top of the header. The light purple on the menu bar is a little dull though. It seems to be grayed out too much. Notice the pop that www.tallyhaven.com has. We need that pop.
-The fonts on the menu bar don't pop either. I don't know if it is because the font is bad or the thickness of the font is bad or what.
-We are not sold on the green color in the logo and header. It is pretty good, but maybe we can test other colors?
Logo Thoughts:
-I am not sold on the green color. It is pretty good, but maybe test it out with some other colors?
-The logo does not pop like the www.tallyhaven.com logo pops.
-We had started thinking about doing an owl as part of our name/logo or maybe some other type of animal. Look at the ideas I had sent our original graphic designer.
A. http://markvista.net/gallery/detail/842907 - i like that is simple, a little abstract, but I don't like that it is sort of evil.
B. http://markvista.net/gallery/detail/27514 - i like that is abstract.
C. http://pixelbrook.files.quillsite.net/2012/05/torvane4.jpg - i like the slightly abstract.
D. http://sketchlark.net/shots/718204-O-W-L - good - abrstract and slightly turned.
Target Market(s)
Sales and Marketing People - primarily a masculine audience in their 20s to 40s.
Industry/Entity Type
Business
Look and feel

```html
<!DOCTYPE html>
<html lang="en">
<head>
<meta charset="utf-8">
<title>Scoutline header</title>
<link rel="stylesheet" href="https://fonts.googleapis.com/css2?family=Arimo:ital,wght@0,400;0,700;1,400&display=swap">
<style>
  :root {
    --slate: #3f4066;
    --violet: #9a00d8;
    --violet-line: #6d1f93;
    --white: #ffffff;
    --lime: #b8c35e;
    --ink: #3f4066;
    --muted: #555a70;
  }
  * { margin: 0; padding: 0; box-sizing: border-box; }
  html, body {
    width: 1200px;
    height: 127px;
    overflow: hidden;
    background: var(--slate);
    font-family: "Arimo", Arial, sans-serif;
  }
  .site-header {
    position: relative;
    width: 1200px;
    height: 127px;
    background: var(--slate);
  }
  .account-tab {
    position: absolute;
    left: 785px;
    top: 0;
    width: 230px;
    height: 34px;
  }
  .account-tab svg { position: absolute; inset: 0; }
  .account-links {
    position: absolute;
    top: 8px;
    left: 34px;
    display: flex;
    gap: 18px;
    font-size: 17px;
    color: var(--white);
    letter-spacing: 0.2px;
  }
  .brand {
    position: absolute;
    left: 58px;
    top: 18px;
    display: flex;
    align-items: center;
    gap: 14px;
  }
  .brand-mark {
    width: 44px;
    height: 44px;
    border-radius: 50%;
    background: var(--violet);
  }
  .brand-name {
    font-size: 40px;
    font-weight: 400;
    color: var(--lime);
    line-height: 1;
  }
  .main-nav {
    position: absolute;
    left: 0;
    top: 80px;
    width: 1200px;
    height: 47px;
    background: var(--violet);
  }
  .nav-list {
    position: absolute;
    left: 172px;
    top: 0;
    display: flex;
    list-style: none;
    height: 47px;
  }
  .nav-item {
    height: 47px;
    display: flex;
    align-items: center;
    justify-content: center;
    font-size: 20px;
    font-weight: 700;
    color: var(--white);
    border-right: 1px solid var(--violet-line);
  }
  .nav-item.is-active {
    background: var(--white);
    color: var(--ink);
    margin-top: 2px;
    height: 45px;
  }
  .nav-new { width: 86px; }
  .nav-people { width: 108px; }
  .nav-companies { width: 152px; }
  .nav-downloads { width: 146px; }
  .search-field {
    position: absolute;
    left: 806px;
    top: 8px;
    width: 265px;
    height: 30px;
    background: var(--white);
    padding: 3px 6px;
    font-size: 21px;
    font-style: italic;
    color: var(--muted);
  }
</style>
</head>
<body>
  <header class="site-header">
    <div class="account-tab">
      <svg width="230" height="34" viewBox="0 0 230 34" aria-hidden="true">
        <polygon points="0,0 230,0 212,34 16,34" fill="var(--violet)"/>
      </svg>
      <div class="account-links">
        <span class="account-link">SIGNUP</span>
        <span class="account-link">LOGIN</span>
      </div>
    </div>

    <div class="brand">
      <span class="brand-mark"></span>
      <span class="brand-name">Scoutline</span>
    </div>

    <nav class="main-nav">
      <ul class="nav-list">
        <li class="nav-item nav-new is-active">New</li>
        <li class="nav-item nav-people">People</li>
        <li class="nav-item nav-companies">Companies</li>
        <li class="nav-item nav-downloads">Downloads</li>
      </ul>
      <div class="search-field">search</div>
    </nav>
  </header>
</body>
</html>
```